BrightLoom business card

We are a performing arts company providing training (to both kids and adults) as well as performers for events. We hope to bring joy and confidence on stage to the people we train, as well as joy to the audience when our artistes perform. Designs should convey the joy, confidence and vibrancy on stage. Design business card using the attached logo. Card to include name, mobile tel, email address, company address, and website. Double sided. To also include the following list of what the company does:
• Training & Enrichment
• Private & Corporate Entertainment
- Music composition & production

Industry/Entity Type

Training

Contact Information for Business Card

Card to include name, mobile tel, email address, company address, and website. Double sided. To also include the following list of what the company does:
• Training & Enrichment

Requirements
Nice to have
• Card need not be the traditional rectangular in shape but not too outrageous.

```html
<!DOCTYPE html>
<html lang="en">
<head>
<meta charset="utf-8">
<title>BrightLoom business card</title>
<link rel="stylesheet" href="https://fonts.googleapis.com/css2?family=Lato:wght@400;700;900&display=swap">
<style>
  :root {
    --backdrop: #2b2b2b;
    --card: #fbfbfb;
    --ink: #333333;
    --navy: #1f3f7a;
    --blue: #1ea6d6;
    --teal: #27b59a;
    --red: #d8262f;
    --pink: #ef5a6b;
    --orange: #f0861e;
    --yellow: #f2b51b;
    --purple: #5b4b8a;
    --magenta: #d81e6a;
  }
  * { box-sizing: border-box; margin: 0; padding: 0; }
  html, body { width: 1200px; height: 873px; overflow: hidden; }
  body {
    background: var(--backdrop);
    font-family: "Lato", Arial, sans-serif;
    position: relative;
  }
  .card {
    position: absolute;
    width: 540px;
    height: 309px;
    background: var(--card);
    border-radius: 4px;
    overflow: hidden;
    box-shadow: 0 10px 30px rgba(0,0,0,.45);
  }
  .card--front { left: 60px; top: 90px; }
  .card--back { left: 600px; top: 474px; }

  .splash {
    position: absolute;
    border-radius: 50% 40% 60% 45%;
  }
  .splash--left {
    background: linear-gradient(135deg, #6fd3e0 0%, var(--orange) 50%, var(--pink) 100%);
  }
  .splash--right {
    background: linear-gradient(160deg, #38c3a4 0%, var(--magenta) 55%, var(--purple) 100%);
  }

  .tabs { position: absolute; display: block; }

  /* front */
  .brand {
    position: absolute;
    left: 160px; top: 92px;
    width: 230px;
    text-align: center;
  }
  .brand__name {
    font-weight: 900;
    font-size: 38px;
    color: var(--pink);
    letter-spacing: .5px;
    display: flex; align-items: center; justify-content: center; gap: 8px;
  }
  .brand__dot {
    width: 14px; height: 14px; border-radius: 50%;
    background: var(--pink);
  }
  .brand__tagline {
    font-weight: 700;
    font-size: 13px;
    color: var(--purple);
    margin-top: 2px;
  }
  .contacts {
    position: absolute;
    right: 30px; top: 92px;
    list-style: none;
    font-size: 12px;
    color: var(--ink);
  }
  .contacts li {
    display: flex; align-items: center; justify-content: flex-end;
    gap: 7px; margin-bottom: 6px;
  }
  .contacts svg { width: 15px; height: 15px; }
  .address {
    position: absolute;
    right: 30px; top: 198px;
    font-size: 12px;
    font-weight: 700;
    color: var(--ink);
  }
  .person {
    position: absolute;
    left: 0; top: 220px;
  }
  .person__name {
    background: var(--blue);
    color: #fff;
    font-size: 22px;
    font-weight: 400;
    padding: 3px 22px 3px 34px;
    border-radius: 0 14px 14px 0;
  }
  .person__name b { font-weight: 700; }
  .person__role {
    font-size: 20px; font-weight: 900;
    color: var(--ink);
    margin: 4px 0 0 70px;
  }

  /* back */
  .back-brand {
    position: absolute;
    left: 0; right: 0; top: 90px;
    text-align: center;
    font-weight: 900;
    font-size: 34px;
    color: var(--navy);
  }
  .services {
    position: absolute;
    left: 0; right: 0; top: 150px;
    list-style: none;
    text-align: center;
    font-weight: 700;
    font-size: 16px;
    line-height: 1.35;
  }
  .services__item--training { color: var(--navy); }
  .services__item--events { color: var(--red); }
  .services__item--music { color: var(--orange); }
</style>
</head>
<body>

<section class="card card--front" aria-label="Front of card">
  <div class="splash splash--left" style="left:18px; top:100px; width:130px; height:95px;" role="img" aria-label="Colourful paint splash with music notes"></div>
  <div class="splash splash--right" style="left:455px; top:10px; width:70px; height:70px;" role="img" aria-label="Colourful paint splash with music notes"></div>

  <div class="brand">
    <div class="brand__name"><span class="brand__dot"></span>BrightLoom</div>
    <div class="brand__tagline">delighting in the arts</div>
  </div>

  <ul class="contacts">
    <li>(555) 014-2290
      <svg viewBox="0 0 16 16"><circle cx="8" cy="8" r="8" fill="var(--blue)"/><rect x="5.5" y="3.5" width="5" height="9" rx="1" fill="#fff"/></svg></li>
    <li>5550 142-2291
      <svg viewBox="0 0 16 16"><circle cx="8" cy="8" r="8" fill="var(--pink)"/><path d="M5 4l2 2-1 1.5c.6 1.2 1.3 1.9 2.5 2.5L10 9l2 2-1.3 1.3C7.5 12 4 8.5 3.7 5.3z" fill="#fff"/></svg></li>
    <li>hello@brightloom.com
      <svg viewBox="0 0 16 16"><circle cx="8" cy="8" r="8" fill="var(--purple)"/><rect x="4" y="5" width="8" height="6" fill="#fff"/><path d="M4 5l4 3 4-3" stroke="var(--purple)" fill="none"/></svg></li>
    <li>27 Harbor Lane, Northfield, AU
      <svg viewBox="0 0 16 16"><circle cx="8" cy="8" r="8" fill="var(--teal)"/><path d="M8 3.5l4.5 4H11v4H5v-4H3.5z" fill="#fff"/></svg></li>
  </ul>

  <svg class="tabs" style="left:250px; top:230px;" width="300" height="90" viewBox="0 0 300 90" aria-hidden="true">
    <rect x="10" y="50" width="70" height="40" rx="8" fill="var(--orange)"/>
    <rect x="60" y="40" width="70" height="50" rx="8" fill="var(--pink)"/>
    <rect x="115" y="30" width="70" height="60" rx="8" fill="var(--purple)"/>
    <rect x="165" y="18" width="70" height="72" rx="8" fill="var(--red)"/>
    <rect x="220" y="8" width="80" height="82" rx="8" fill="var(--blue)"/>
  </svg>

  <div class="person">
    <div class="person__name">Daniel <b>Verhoek</b></div>
    <div class="person__role">Owner</div>
  </div>
</section>

<section class="card card--back" aria-label="Back of card">
  <svg class="tabs" style="left:120px; top:0;" width="420" height="40" viewBox="0 0 420 40" aria-hidden="true">
    <rect x="0" y="-10" width="80" height="34" rx="8" fill="var(--orange)"/>
    <rect x="70" y="-10" width="80" height="30" rx="8" fill="var(--pink)"/>
    <rect x="140" y="-10" width="80" height="26" rx="8" fill="var(--purple)"/>
    <rect x="210" y="-10" width="80" height="22" rx="8" fill="var(--red)"/>
    <rect x="280" y="-10" width="70" height="18" rx="8" fill="var(--blue)"/>
    <rect x="340" y="-10" width="80" height="14" rx="8" fill="var(--yellow)"/>
  </svg>

  <div class="splash splash--left" style="left:20px; top:110px; width:120px; height:110px;" role="img" aria-label="Colourful paint splash with music notes"></div>
  <div class="splash splash--right" style="left:440px; top:60px; width:80px; height:100px;" role="img" aria-label="Colourful paint splash with music notes"></div>

  <div class="back-brand">BrightLoom</div>

  <ul class="services">
    <li class="services__item--training">Training &amp; Enrichment</li>
    <li class="services__item--events">Private &amp; Corporate Entertainment</li>
    <li class="services__item--music">Music Composition &amp; Production</li>
  </ul>

  <svg class="tabs" style="left:0; top:259px;" width="540" height="50" viewBox="0 0 540 50" aria-hidden="true">
    <rect x="20" y="30" width="90" height="30" rx="8" fill="var(--orange)"/>
    <rect x="95" y="22" width="90" height="38" rx="8" fill="var(--pink)"/>
    <rect x="170" y="16" width="90" height="44" rx="8" fill="var(--purple)"/>
    <rect x="245" y="8" width="90" height="52" rx="8" fill="var(--red)"/>
    <rect x="390" y="0" width="80" height="60" rx="8" fill="var(--blue)"/>
    <rect x="455" y="4" width="85" height="56" rx="8" fill="var(--pink)"/>
  </svg>
</section>

</body>
</html>
```